IT consulting company looking for a modern business design for a website and a new logo

We are the IT-consulting company VelTarix from Germany and need a new and modern business website and a new logo. We are specialized in output management. Our services include business analysis, outsourcing, development, training and project leading. We wish for a design with nature pictures (mountains, lakes, rivers, forests, etc.) for our company with the colors green and blue. If it is possible, a slow-mo video of a nature scene. The design should be responsive and the menu should change to a hamburger menu. The following are: • Services / Solutions 1. Output Management 2. Outsourcing 3. Development 4. Business Analyst 5. Training • Partners • Careers • About Us 1. Project A 2. Project B 3. Project C • Contact Notes for the following categories: For "Services / Solutions" we want to conclude some contents from all the sub-points and sub-points below. Additionally, we would like to see some sub-point under "Services / Solutions". For Output Management: "5 Benefits of Output Management Systems (OMS) - OMS Simplifies and Accelerates External Communication - Helps Reduce Communication Mistakes - Provides Customers With Fast and Secure Responses to your questions - Employees can focus on the essential as they can access prepared templates - Companies get complete transparency about their communication "The point" partner does not have sub-points. The content here is a quote and the logo from the company Brin. For now, just placeholders on this site. The next point wants to be "career" without sub-point and wants to contain some text. Carrer options wants to be listed here. Next point wants to be "About us", where we need sub-points which we do not know exactly at this moment, but they will contain text. By clicking directly on "About us" we want to include pictures and texts about 6 employees for which we only need placeholders at the moment. The last point wants to be "contact", where customers can send us messages. The main page should include a story about our company, which can be a placeholder for now. For reference, designs have a look at: https://lumoravex.de/ https://www.trobelink.com/ https://www.pemdarix.de/ We prefer WordPress designs, created with the plugin ELEMENTOR, so that we can easily edit the content by ourselves. The final design should look professional, competent and modern.

Target Market(s)

With our website, we want to reach the following target groups. <br> <br> <br> <br> <br> <br> <br> <br> <br> <br> <br> <br> <br> <br> <br> <br> <br> <br> <br> <br> <br> <br> <br> <br> <br> <br> <br> <br> <br> <br> <br> <br> <br> <br> <br> <br> <br> <br> <br> <br> <br> <br> <br> <br> <br> <br> <br> <br> <br>

Industry/Entity Type

Consulting

Logo Text

(optionally) VelTarix

Font styles to use
Sans Serif

Colors

Designer to choose colors to be used in the design.

Requirements
Must have
• 1. Outsourcing 3. Development 4. Business Analyst 5. Training • Partners • Careers • About Us 1. Project A 2. Project B 3. Project C • Contact The above-mentioned background picture with nature motifs (mountains, lakes, rivers, forests, etc.). WordPress design in primary colors blue and green.
Nice to have
• ELEMENTOR template. Effects for the background pictures. Counter of all successful projects for Output Management, Business Analyst and Training

```html
<!DOCTYPE html>
<html lang="en">
<head>
<meta charset="utf-8">
<title>VelTarix – IT Consulting</title>
<link href="https://fonts.googleapis.com/css2?family=Open+Sans:wght@400;600;700&display=swap" rel="stylesheet">
<style>
:root{
  --blue:#3aaee0;
  --green:#8cc63f;
  --green-light:#9fd36a;
  --ink:#222;
  --text:#444;
  --muted:#777;
  --line:#e2e2e2;
  --footer:#141311;
  --white:#fff;
}
*{box-sizing:border-box;margin:0;padding:0}
html,body{width:1200px;height:3371px;overflow:hidden}
body{font-family:"Open Sans",Arial,sans-serif;color:var(--text);background:var(--white);position:relative}
.abs{position:absolute}

/* header */
.topline{left:0;top:0;width:1200px;height:7px;background:var(--blue)}
.header{left:0;top:7px;width:1200px;height:101px;background:var(--white)}
.brand{left:120px;top:28px;display:flex;align-items:center;gap:10px}
.brand-mark{width:22px;height:22px;background:var(--green)}
.brand-name{font-size:26px;font-weight:700;color:var(--green);letter-spacing:.5px}
.callus{left:698px;top:28px;font-size:16px;color:var(--ink);display:flex;align-items:center;gap:8px}
.callus b{color:var(--green);font-weight:600}
.social{left:944px;top:30px;display:flex;gap:20px}
.social span{width:15px;height:15px;border:1.5px solid #444;border-radius:3px;display:block}
.nav{left:612px;top:74px;display:flex;gap:48px;font-size:14px;color:var(--ink)}

/* hero */
.hero{left:0;top:108px;width:1200px;height:545px;background:linear-gradient(180deg,#d8d8d8 0%,#eeeeee 35%,#bdbdbd 70%,#8f8f8f 100%)}
.hero-cut{left:0;top:560px}
.hero-arrow{top:340px;width:48px;height:42px;background:rgba(90,90,90,.75);display:flex;align-items:center;justify-content:center}
.hero-sub{left:0;width:1200px;top:352px;text-align:center;font-size:32px;color:var(--blue);letter-spacing:1px}
.hero-title{left:0;width:1200px;top:388px;text-align:center;font-size:44px;font-weight:600;color:var(--blue);letter-spacing:1px}
.btn{display:inline-block;background:var(--green);color:var(--white);font-size:12px;font-weight:600;text-align:center}
.hero-btn{left:532px;top:468px;width:144px;height:40px;line-height:40px;border-radius:20px}

/* section title */
.sec-icon{width:20px;height:20px;background:var(--green)}
.sec-title{left:0;width:1200px;text-align:center;font-size:34px;color:var(--blue);font-weight:600;letter-spacing:.5px}
.sec-rule{width:62px;height:2px;background:var(--blue);left:569px}

/* services */
.card{top:834px;width:225px;height:320px;background:#f4f4f4;border:1px solid var(--line)}
.card .ph{width:100%;height:184px;background:linear-gradient(160deg,#5b7b94,#2d4a61)}
.card h3{font-size:15px;font-weight:400;color:var(--blue);margin:22px 0 0 24px}
.card p{font-size:11px;line-height:18px;color:var(--text);margin:10px 12px 0 24px}
.card .more{font-size:11px;color:var(--blue);margin:14px 0 0 24px}
.card.active{background:var(--blue);border-color:var(--blue)}
.card.active h3,.card.active p,.card.active .more{color:var(--white)}

/* about */
.about-h{left:121px;top:1326px;font-size:21px;font-weight:600;color:var(--ink);letter-spacing:.5px}
.about-p{left:121px;width:440px;font-size:13px;line-height:21px;color:var(--ink)}
.about-btn{left:121px;top:1554px;width:120px;height:40px;line-height:40px;background:var(--green-light);font-weight:400}
.about-photo{left:675px;top:1316px;width:375px;height:302px;background:linear-gradient(160deg,#cfd4cf 0%,#8e9a9e 50%,#4d5a62 100%)}

/* benefits */
.band{left:0;top:1692px;width:1200px;height:398px;background:linear-gradient(100deg,#c9c5bd 0%,#8e8a82 45%,#6b5334 75%,#b07a36 100%)}
.oms{left:281px;top:1730px;width:640px;height:319px;background:rgba(70,70,70,.72);color:var(--white);padding:28px 30px}
.oms h2{font-size:17px;font-weight:600;letter-spacing:.3px;margin-bottom:14px}
.oms ul{list-style:none}
.oms li{font-size:12.5px;line-height:29px;padding-left:22px;position:relative}
.oms li .chev{position:absolute;left:0;top:9px}
.oms-btn{left:548px;top:1995px;width:108px;height:36px;line-height:36px;background:var(--green-light);font-weight:400}

/* testimonials */
.testi-bg{left:0;top:2090px;width:1200px;height:561px;background:linear-gradient(180deg,#f2f3f4,#dfe3e6 60%,#c9d2d8)}
.quote{left:362px;top:2265px;width:481px;height:270px;background:var(--white);box-shadow:0 2px 8px rgba(0,0,0,.15);text-align:center}
.quote p{font-size:11.5px;line-height:19px;color:var(--ink);width:250px;margin:30px auto 0}
.qmark{position:absolute;font-size:40px;color:#aaa;font-weight:700;line-height:1}
.avatar{width:70px;height:70px;border-radius:50%;background:#ddd;border:2px solid #bbb;margin:18px auto 0;display:flex;align-items:center;justify-content:center;font-size:11px;color:var(--ink);font-weight:600}
.quote h4{font-size:14px;color:var(--ink);margin-top:14px}
.quote small{font-size:11px;color:var(--muted)}
.qarrow{top:2388px;width:22px;height:22px;border:1.5px solid #555;border-radius:50%}

/* cta */
.cta{left:0;top:2651px;width:1200px;height:234px;background:linear-gradient(90deg,var(--green-light) 0%,#7fc8b0 50%,var(--blue) 100%)}
.cta-photo{left:30px;top:2598px;width:375px;height:287px;background:linear-gradient(180deg,#b9a79a 0%,#6f5f58 45%,#dcdcdc 100%)}
.cta-text{left:598px;top:2696px;width:520px;font-size:20px;line-height:33px;font-weight:600;color:var(--white)}
.cta-btn{left:600px;top:2803px;width:122px;height:42px;line-height:42px;background:var(--white);color:var(--green);font-weight:400}

/* footer */
.footer{left:0;top:2885px;width:1200px;height:486px;background:var(--footer)}
.f-h{font-size:16px;font-weight:700;color:var(--white);letter-spacing:.3px}
.f-links{list-style:none;font-size:12.5px;color:var(--white);line-height:29px}
.f-row{display:flex;align-items:center;gap:20px;font-size:15px;color:var(--green);line-height:28px}
.f-follow{display:flex;gap:18px}
.f-follow span{width:15px;height:15px;border:1.5px solid #ccc;border-radius:3px;display:block}
.field{left:762px;width:321px;height:42px;border:1px solid #bbb;border-radius:3px;font-size:12px;color:var(--white);padding:12px 16px}
.submit{left:762px;top:3245px;width:321px;height:42px;line-height:42px;background:var(--white);color:var(--blue);font-size:13px;font-weight:600;text-align:center;border-radius:3px}
.f-line{left:0;top:3316px;width:1200px;height:1px;background:#333}
.copy{left:0;width:1200px;top:3340px;text-align:center;font-size:11px;color:var(--white)}
</style>
</head>
<body>

<div class="abs topline"></div>
<header class="abs header"></header>
<div class="abs brand"><span class="brand-mark"></span><span class="brand-name">VelTarix</span></div>
<div class="abs callus">
  <b>Call Us:</b>
  <svg width="16" height="16" viewBox="0 0 24 24"><path d="M6.6 10.8a15 15 0 0 0 6.6 6.6l2.2-2.2a1 1 0 0 1 1-.25 11.4 11.4 0 0 0 3.6.57 1 1 0 0 1 1 1V20a1 1 0 0 1-1 1A17 17 0 0 1 3 4a1 1 0 0 1 1-1h3.5a1 1 0 0 1 1 1c0 1.25.2 2.45.57 3.57a1 1 0 0 1-.25 1z" fill="#8cc63f"/></svg>
  <span>+123-456-7890</span>
</div>
<div class="abs social"><span></span><span></span><span></span><span></span></div>
<nav class="abs nav"><span>Home</span><span>About Us</span><span>Service</span><span>Carrier</span><span>Contact Us</span></nav>

<section class="abs hero" role="img" aria-label="Misty grey mountain peaks under clouds"></section>
<svg class="abs hero-cut" width="1200" height="100" viewBox="0 0 1200 100"><polygon points="0,13 600,95 1200,13 1200,100 0,100" fill="#fff"/></svg>
<div class="abs hero-arrow" style="left:0;border-radius:0 21px 21px 0"><svg width="12" height="14"><path d="M9 1 3 7l6 6" stroke="#fff" stroke-width="2" fill="none"/></svg></div>
<div class="abs hero-arrow" style="left:1152px;border-radius:21px 0 0 21px"><svg width="12" height="14"><path d="M3 1l6 6-6 6" stroke="#fff" stroke-width="2" fill="none"/></svg></div>
<div class="abs hero-sub">LET US PROVIDE</div>
<h1 class="abs hero-title">THE SUPPORT YOU DESERVE</h1>
<div class="abs btn hero-btn">Contact Us</div>

<div class="abs sec-icon" style="left:590px;top:705px"></div>
<h2 class="abs sec-title" style="top:736px">SERVICES</h2>
<div class="abs sec-rule" style="top:788px"></div>

<article class="abs card" style="left:121px"><div class="ph" role="img" aria-label="Team meeting in front of a presentation screen"></div><h3>Business Analyst</h3><p>Lorem ipsum dolor sit amet, conec nostrud exercitation ullamco.</p><div class="more">Read More &nbsp;›</div></article>
<article class="abs card active" style="left:364px"><div class="ph" role="img" aria-label="Businessman touching an outsourcing network interface"></div><h3>Outsourcing</h3><p>Lorem ipsum dolor sit amet, conec nostrud exercitation ullamco.</p><div class="more">Read More &nbsp;›</div></article>
<article class="abs card" style="left:613px"><div class="ph" role="img" aria-label="Training class with people at laptops"></div><h3>Training</h3><p>Lorem ipsum dolor sit amet, conec nostrud exercitation ullamco.</p><div class="more">Read More &nbsp;›</div></article>
<article class="abs card" style="left:856px"><div class="ph" role="img" aria-label="Financial charts on a screen"></div><h3>Devlopment</h3><p>Lorem ipsum dolor sit amet, conec nostrud exercitation ullamco.</p><div class="more">Read More &nbsp;›</div></article>

<div class="abs sec-icon" style="left:590px;top:1203px"></div>
<h2 class="abs sec-title" style="top:1230px">ABOUT</h2>
<div class="abs sec-rule" style="top:1282px"></div>

<h3 class="abs about-h">OUR COMPANY</h3>
<p class="abs about-p" style="top:1363px">Lorem ipsum dolor sit amet, consectetur adipiscing elit, sed do eiusmod tempor incididunt ut labore et dolore magna aliqua. Ut enim ad minim veniam, quis nostrud exercitation ullamco laboris nisi ut aliquip ex ea commodo consequat.</p>
<p class="abs about-p" style="top:1461px">Duis aute irure dolor in reprehenderit in voluptate velit esse cillum dolore eu fugiat nulla pariatur. Excepteur sint occaecat cupidatat non proident, sunt in culpa qui officia deserunt mollit anim id est laborum.</p>
<div class="abs btn about-btn">MORE INFO</div>

<div class="abs about-photo" role="img" aria-label="Desktop computer showing a business team meeting"></div>

<section class="abs band" role="img" aria-label="Sunset coastline with cliffs and sea"></section>
<div class="abs oms">
  <h2>5 VORTEILE VON OUTPUT MANAGEMENT SYSTEMEN (OMS)</h2>
  <ul>
    <li><svg class="chev" width="12" height="10"><path d="M1 1l4 4-4 4M6 1l4 4-4 4" stroke="#fff" stroke-width="1.5" fill="none"/></svg>OMS vereinfacht und beschleunigt die Kommunikation mit Außen.</li>
    <li><svg class="chev" width="12" height="10"><path d="M1 1l4 4-4 4M6 1l4 4-4 4" stroke="#fff" stroke-width="1.5" fill="none"/></svg>Hilft dabei Fehler bei der Kommunikation zu reduzieren.</li>
    <li><svg class="chev" width="12" height="10"><path d="M1 1l4 4-4 4M6 1l4 4-4 4" stroke="#fff" stroke-width="1.5" fill="none"/></svg>Kunden erhalten schnell und sicher antworten auf Ihre Fragen.</li>
    <li><svg class="chev" width="12" height="10"><path d="M1 1l4 4-4 4M6 1l4 4-4 4" stroke="#fff" stroke-width="1.5" fill="none"/></svg>Mitarbeiter können sich auf das wesentliche konzentrieren, da sie auf</li>
    <li>vorbereitete Vorlagen zurückgreifen können.</li>
    <li><svg class="chev" width="12" height="10"><path d="M1 1l4 4-4 4M6 1l4 4-4 4" stroke="#fff" stroke-width="1.5" fill="none"/></svg>Unternehmen erhalten vollständige Transparenz über Ihre Kommunikation.</li>
  </ul>
</div>
<div class="abs btn oms-btn">Contact Us</div>

<section class="abs testi-bg" role="img" aria-label="Misty lake with trees in soft light"></section>
<div class="abs sec-icon" style="left:590px;top:2135px"></div>
<h2 class="abs sec-title" style="top:2162px">WHAT OVER PARTNER SAY</h2>
<div class="abs sec-rule" style="top:2212px"></div>

<div class="abs quote">
  <span class="qmark" style="left:66px;top:16px">“</span>
  <span class="qmark" style="right:80px;top:84px">”</span>
  <p>Lorem ipsum dolor sit amet, consectetur adipi minim veniam,co labris nisi ut aliquip com veniam,co labris nisi ut aliquip com nisi ut aliquip com</p>
  <div class="avatar"><span style="width:8px;height:8px;background:#aaa;border-radius:50%;margin-right:4px;display:inline-block"></span>Tidora</div>
  <h4>Tidora</h4>
  <small>Cleaning Compny</small>
</div>
<div class="abs qarrow" style="left:386px"><svg width="19" height="19"><path d="M11 5 7 9.5l4 4.5" stroke="#555" stroke-width="1.5" fill="none"/></svg></div>
<div class="abs qarrow" style="left:797px"><svg width="19" height="19"><path d="M8 5l4 4.5L8 14" stroke="#555" stroke-width="1.5" fill="none"/></svg></div>

<section class="abs cta"></section>
<div class="abs cta-photo" role="img" aria-label="Businesswoman working on a laptop"></div>
<p class="abs cta-text">Have big plans, We are looking for really good people,who want to move something with us!</p>
<div class="abs btn cta-btn">MORE INFO</div>

<footer class="abs footer"></footer>
<h4 class="abs f-h" style="left:121px;top:2958px">QUICK LINK</h4>
<ul class="abs f-links" style="left:121px;top:2993px"><li>About Us</li><li>Service</li><li>Carrier</li><li>Contact Us</li></ul>

<h4 class="abs f-h" style="left:366px;top:2958px">CONTACT US</h4>
<div class="abs" style="left:366px;top:2996px">
  <div class="f-row"><svg width="14" height="14" viewBox="0 0 24 24"><path d="M6.6 10.8a15 15 0 0 0 6.6 6.6l2.2-2.2a1 1 0 0 1 1-.25 11.4 11.4 0 0 0 3.6.57 1 1 0 0 1 1 1V20a1 1 0 0 1-1 1A17 17 0 0 1 3 4a1 1 0 0 1 1-1h3.5a1 1 0 0 1 1 1c0 1.25.2 2.45.57 3.57a1 1 0 0 1-.25 1z" fill="#fff"/></svg><span>123-456-7890</span></div>
  <div class="f-row"><svg width="14" height="14" viewBox="0 0 24 24"><rect x="2" y="5" width="20" height="14" fill="none" stroke="#fff" stroke-width="2"/><path d="M2 5l10 8 10-8" fill="none" stroke="#fff" stroke-width="2"/></svg><span>Lorem@xyz.com.</span></div>
  <div class="f-row"><svg width="14" height="14" viewBox="0 0 24 24"><path d="M12 2a7 7 0 0 0-7 7c0 5 7 13 7 13s7-8 7-13a7 7 0 0 0-7-7z" fill="none" stroke="#fff" stroke-width="2"/><circle cx="12" cy="9" r="2.5" fill="#fff"/></svg><span>Lorem road,abc bz lfy</span></div>
  <div class="f-row"><span style="width:14px"></span><span>Germany</span></div>
</div>
<h4 class="abs f-h" style="left:366px;top:3130px;font-size:13px">Follow Us</h4>
<div class="abs f-follow" style="left:366px;top:3165px"><span></span><span></span><span></span><span></span></div>

<h4 class="abs f-h" style="left:762px;top:2958px">GENERAL ENQUIRIES</h4>
<div class="abs field" style="top:3004px">Your Name*</div>
<div class="abs field" style="top:3052px">Your Email*</div>
<div class="abs field" style="top:3100px">Phone Number*</div>
<div class="abs field" style="top:3148px;height:82px">Message*</div>
<div class="abs submit">SUBMIT</div>

<div class="abs f-line"></div>
<div class="abs copy">Copyright© 2019 veltarix.</div>

</body>
</html>
```